HVAC company business card design

We need a business card design for a HVAC company. The design must look professional. Both sides will be used. The total data to be on the business card is
Name
Position
Email
Direct Phone/Moile Phone
Company Contacts /Address, Phone, Fax, web)
All data will be submit once the design is confirmed. For generic purposes use;
Emre Toksoy
Managing Director
+902324815263 (Mobile)
4712 Sokak No: 9 KBSE Yenikent IZMIR TURKEY
Tel: +902324815263 Fax : +902324815269
www.luvon.com.tr

Target Market(s)

HVAC

Industry/Entity Type

Business

Contact Information for Business Card

The total data to be on the business card is
Name
Position
Email
Direct Phone/Moile Phone
Emre Toksoy
Managing Director
+902324815263 (Mobile)
www.luvon.com.tr
The BC will use both sides of the card. The front will include the full logo and the details for the business card holder. The business card can be divided into vertical/horizontal or to a special shape. The common data like the company address/phone/fax should be indicated elsewehere. The back can contain some part or the whole logo and must contain the web address.

Font styles to use
Serif
Sans Serif

Colors
0355a3
cfdfed

Requirements
Should not have
• Please be careful with the fonts, it shouldnt be too small or too big and must not interfere with the logo fonts. If you need to use a curvy shape please do not use as the logo is already curvy or use the curves from the logo (if it looks good, otherwise forget it)
• We are not in favor of pictograms, only if they are perfect use them.

```html
<!DOCTYPE html>
<html lang="en">
<head>
<meta charset="utf-8">
<title>Luvon business card</title>
<link rel="stylesheet" href="https://fonts.googleapis.com/css2?family=Open+Sans:wght@400;600;700&display=swap">
<style>
  :root {
    --backdrop: #eef1f5;
    --paper: #ffffff;
    --navy: #3d4660;
    --blue-light: #4fb6f0;
    --blue-deep: #2b68d0;
    --brand-blue: #0355a3;
    --back-centre: #5e9ce6;
    --back-edge: #2f6bd0;
    --ink-light: #ffffff;
  }
  * { margin: 0; padding: 0; box-sizing: border-box; }
  html, body {
    width: 1200px; height: 900px; overflow: hidden;
    background: var(--backdrop);
    font-family: "Open Sans", Arial, sans-serif;
  }
  .canvas { position: relative; width: 1200px; height: 900px; }

  .card { position: absolute; overflow: hidden; box-shadow: 0 6px 18px rgba(0,0,0,.18); }

  /* Front */
  .card-front { left: 78px; top: 33px; width: 587px; height: 364px; background: var(--paper); }
  .card-front .bands { position: absolute; inset: 0; }
  .brand-lockup {
    position: absolute; left: 0; right: 0; top: 52px;
    display: flex; justify-content: center; align-items: center; gap: 16px;
  }
  .brand-dot { width: 58px; height: 58px; border-radius: 50%; background: var(--brand-blue); }
  .brand-name {
    font-size: 56px; font-weight: 700; letter-spacing: 3px; color: var(--navy); line-height: 1;
  }
  .contact-list {
    position: absolute; top: 210px; right: 326px; list-style: none;
    color: var(--ink-light); font-size: 15px;
  }
  .contact-list li {
    display: flex; justify-content: flex-end; align-items: center; gap: 10px;
    height: 24.5px;
  }
  .contact-list svg { width: 12px; height: 12px; flex: none; }
  .holder { position: absolute; left: 305px; top: 208px; color: var(--ink-light); }
  .holder-name { font-size: 20px; font-weight: 600; line-height: 28px; }
  .holder-role { font-size: 15px; line-height: 20px; }
  .holder-address { margin-top: 28px; font-size: 15px; line-height: 24.5px; }

  /* Back */
  .card-back {
    left: 388px; top: 505px; width: 567px; height: 352px;
    background: radial-gradient(circle at 50% 55%, var(--back-centre) 0%, var(--back-edge) 62%);
    color: var(--ink-light); text-align: center;
  }
  .back-name {
    position: absolute; left: 0; right: 0; top: 108px;
    font-size: 76px; font-weight: 700; letter-spacing: 5px; line-height: 1;
  }
  .back-web {
    position: absolute; left: 0; right: 0; top: 218px;
    font-size: 17px; font-weight: 700;
  }
</style>
</head>
<body>
<main class="canvas">

  <section class="card card-front" aria-label="Business card front">
    <svg class="bands" width="587" height="364" viewBox="0 0 587 364" aria-hidden="true">
      <defs>
        <linearGradient id="frontBlue" x1="0" y1="0" x2="0" y2="1">
          <stop offset="0" stop-color="var(--blue-light)" style="stop-color:#4fb6f0"/>
          <stop offset="1" stop-color="#2b68d0"/>
        </linearGradient>
      </defs>
      <polygon points="0,167 398,167 378,193 0,193" fill="#3d4660"/>
      <polygon points="0,196 382,196 414,160 587,160 587,364 0,364" fill="url(#frontBlue)"/>
    </svg>

    <div class="brand-lockup">
      <span class="brand-dot"></span>
      <span class="brand-name">LUVON</span>
    </div>

    <ul class="contact-list">
      <li>+902324815263
        <svg viewBox="0 0 12 12"><rect x="3" y="0.5" width="6" height="11" rx="1" fill="none" stroke="#fff" stroke-width="1.3"/><circle cx="6" cy="9.5" r=".8" fill="#fff"/></svg></li>
      <li>+902324815263
        <svg viewBox="0 0 12 12"><path d="M2 1l2 0 1 3-1.3 1a6 6 0 0 0 3.3 3.3L8 7l3 1v2a1 1 0 0 1-1 1A9 9 0 0 1 1 2a1 1 0 0 1 1-1z" fill="#fff"/></svg></li>
      <li>+902324815269
        <svg viewBox="0 0 12 12"><rect x="1" y="4" width="10" height="7" rx="1" fill="#fff"/><rect x="3" y="1" width="6" height="4" fill="none" stroke="#fff"/></svg></li>
      <li>info@luvon.com.tr
        <svg viewBox="0 0 12 12"><rect x="0.5" y="2.5" width="11" height="7.5" fill="#fff"/><path d="M0.5 2.5l5.5 4 5.5-4" fill="none" stroke="#3a84dc" stroke-width="1"/></svg></li>
      <li>www.luvon.com.tr
        <svg viewBox="0 0 12 12"><circle cx="6" cy="6" r="5.3" fill="#fff"/><path d="M1 6h10M6 .7c-2.4 2.8-2.4 7.8 0 10.6M6 .7c2.4 2.8 2.4 7.8 0 10.6" fill="none" stroke="#3a84dc" stroke-width=".8"/></svg></li>
    </ul>

    <div class="holder">
      <p class="holder-name">Emre Toksoy</p>
      <p class="holder-role">Managing Director</p>
      <p class="holder-address">4712 Sokak No: 9 KBSE<br>Yenikent IZMIR TURKEY</p>
    </div>
  </section>

  <section class="card card-back" aria-label="Business card back">
    <p class="back-name">LUVON</p>
    <p class="back-web">www.luvon.com.tr</p>
  </section>

</main>
</body>
</html>
```